Cloud Software Services Business Needs New Website Design

Our client is looking for a really modern design for their cloud services company. We have a logo, but apart from that, if you read the brief fully and digest the wireframes, we hope you will come up with a really amazing end product.

The design of the website should be professional and trustworthy, it is there to inspire confidence in the services and softwares, as well as emphasising the track record of RMV and relative knowledge and competencies.

Given all the cloud-related communications in the messaging on the site, we will need this in either the imagery or icons in the site so that we can connect the messaging with the service offering.

The brand, being black, gives full range for the designer to present a palette that serves the brand, not forgetting the audience are generally IT decision-makers.

Target Market(s)

Managers and Directors Responsible for IT/Cloud Infrastructure

Industry/Entity Type

IT Technology

Number of Pages Required

5+ page

Font styles to use
Sans Serif

Requirements
Must have
• Initial designs which match the brief and wireframes, focus on the homepage and the winning designer will need to supply the internal pages for the website.
Nice to have
• Clearly considered professional website designs, with consistent design work and branding. If choosing stock imagery, then from PixHarbor Basics please.
Should not have
• Not too much colour, or too consumer/youthful.

```html
<!DOCTYPE html>
<html lang="en">
<head>
<meta charset="utf-8">
<title>RMV – Cloud Services</title>
<link href="https://fonts.googleapis.com/css2?family=Raleway:wght@400;500;600;700&family=Open+Sans:wght@400;600&display=swap" rel="stylesheet">
<style>
:root{
  --navy:#08173a;
  --navy-2:#0d3676;
  --blue:#1257b8;
  --blue-mid:#1673cc;
  --sky:#2f9be0;
  --ink:#111a2c;
  --text:#4a4f5c;
  --muted:#8a8f9b;
  --line:#e3e7ee;
  --pale:#e7f1fb;
  --white:#fff;
}
*{box-sizing:border-box;margin:0;padding:0}
html,body{width:1200px;height:4766px;overflow:hidden}
body{font-family:"Open Sans",Arial,sans-serif;color:var(--text);background:var(--white);position:relative}
h1,h2,h3,h4,.head{font-family:"Raleway",Arial,sans-serif;font-weight:500}
.section{position:absolute;left:0;width:1200px}
.abs{position:absolute}
.accent{color:var(--blue-mid)}
.btn{display:inline-flex;align-items:center;justify-content:center;height:42px;border-radius:21px;font-family:"Raleway",sans-serif;font-size:15px;font-weight:500;letter-spacing:.3px}
.btn-solid{background:linear-gradient(90deg,var(--blue),var(--blue-mid));color:#fff;padding:0 26px}
.btn-outline{border:2px solid var(--blue);color:var(--blue);padding:0 20px;gap:8px;font-size:19px;background:#fff}
.sec-title{text-align:center;font-size:34px;line-height:41px;color:var(--ink);text-transform:uppercase;letter-spacing:-.3px}

/* header */
.site-header{top:0;height:85px;border-bottom:1px solid var(--line)}
.brand{left:60px;top:18px;font-family:"Raleway",sans-serif;font-weight:700;font-size:40px;color:#000;letter-spacing:1px}
.nav-top{right:60px;top:12px;display:flex;gap:26px;font-size:10.5px;color:var(--muted);letter-spacing:.5px;font-family:"Raleway",sans-serif}
.nav-rule{left:752px;right:58px;top:33px;height:1px;background:var(--line)}
.nav-main{right:62px;top:54px;display:flex;gap:38px;font-size:11px;color:var(--ink);letter-spacing:.5px;font-family:"Raleway",sans-serif;font-weight:600}
.nav-main .on{color:var(--sky)}

/* hero */
.hero{top:85px;height:627px;background:linear-gradient(100deg,#061232 0%,#0a2a5e 45%,#0c3370 100%)}
.hero-art{left:520px;top:0;width:680px;height:627px;background:radial-gradient(circle at 55% 45%,#6fd3ff 0%,#2a7fd6 22%,#17439a 45%,rgba(8,23,58,0) 72%)}
.hero h1{left:58px;top:150px;font-size:50px;line-height:54px;color:#fff;text-transform:uppercase;letter-spacing:.5px}
.hero-sub{left:62px;top:272px;font-size:24px;color:var(--sky);font-family:"Raleway",sans-serif;letter-spacing:.5px}
.tiles{left:60px;top:350px;display:flex;gap:8px}
.tile{width:135px;height:140px;border-radius:12px;background:rgba(40,120,210,.35);display:flex;flex-direction:column;align-items:center;padding-top:22px;color:#fff;font-family:"Raleway",sans-serif;font-size:13px;text-align:center;line-height:18px}
.tile svg{margin-bottom:12px}

/* promise */
.promise{top:712px;height:630px}
.promise .sec-title{position:absolute;top:70px;width:100%}
.promise-copy{left:115px;top:200px;width:520px;font-size:12px;line-height:21px}
.promise-copy p{margin-bottom:10px}
.promise-copy .lead{font-size:14px;color:var(--ink);margin-top:12px;line-height:23px}
.promise-copy ol{padding-left:20px;font-size:13px;color:var(--ink);line-height:30px;margin-top:10px}
.promise-copy .call{color:var(--blue-mid);font-size:14px;margin-top:12px}
.promise-btns{left:113px;top:525px;display:flex;gap:8px}
.device{left:690px;top:275px;width:390px;height:248px;border-radius:10px 10px 0 0;background:linear-gradient(180deg,#e8ecf2 0%,#c9d3e2 55%,#3f63c9 100%)}
.device-base{left:625px;top:523px;width:520px;height:16px;border-radius:0 0 14px 14px;background:#e4e7eb}

/* tools pill */
.tools{top:1353px;left:61px;width:1078px;height:422px;border-radius:0 211px 211px 211px;background:linear-gradient(90deg,#0b4fb0 0%,#1668c4 50%,#169be0 100%)}
.tools-art{left:150px;top:50px;width:320px;height:320px;border-radius:50%;background:radial-gradient(circle,rgba(255,255,255,.35) 0%,rgba(255,255,255,.1) 45%,rgba(255,255,255,0) 70%)}
.tools h2{left:526px;top:128px;font-size:34px;color:#fff;text-transform:uppercase}
.tools p{left:527px;top:185px;font-size:14px;color:#cfe5fa;font-family:"Raleway",sans-serif}
.tools .btn{left:530px;top:228px;background:#0d4aa3;color:#fff;padding:0 28px;position:absolute}

/* providers */
.move{top:1775px;height:515px}
.move .sec-title{position:absolute;top:70px;width:100%}
.cards{left:178px;top:190px;display:flex;gap:36px}
.card{width:257px;height:277px;border-radius:16px;background:#fff;box-shadow:0 4px 14px rgba(20,40,80,.12);text-align:center;padding-top:46px}
.card .name{font-family:"Raleway",sans-serif;font-size:30px;font-weight:600;color:var(--ink);height:50px}
.card p{font-size:11.5px;line-height:20px;padding:10px 22px 0}
.card .btn{margin-top:14px;padding:0 22px;height:40px}
.arrow{top:313px}

/* advice */
.advice{top:2290px;height:323px;text-align:center}
.advice .sec-title{position:absolute;top:24px;width:100%}
.advice-copy{left:290px;top:130px;width:620px;font-size:12px;line-height:21px}
.advice-copy p{margin-bottom:14px}

/* costs */
.costs{top:2613px;height:442px;background:linear-gradient(120deg,#071838 0%,#0d2f62 50%,#0a2450 100%)}
.costs .sec-title{position:absolute;top:70px;width:100%;color:#fff}
.costs .sec-title .accent{color:var(--blue-mid)}
.ring{left:262px;top:156px}
.cost-copy{left:495px;top:180px;width:460px;font-size:12.5px;line-height:21px;color:#e2ebf7}
.cost-copy p{margin-bottom:14px}
.costs .btn{position:absolute;left:492px;top:323px;padding:0 22px;background:var(--blue-mid);color:#fff}

/* start */
.start{top:3055px;height:356px}
.start h2{left:168px;top:80px;font-size:34px;color:var(--ink);text-transform:uppercase}
.start p{left:168px;top:140px;width:420px;font-size:12.5px;line-height:21px}
.start-btns{left:168px;top:215px;display:flex;gap:8px}
.person{left:690px;top:55px;width:270px;height:301px;background:linear-gradient(180deg,#dfe4ea 0%,#3a4452 70%,#1b222c 100%);border-radius:130px 130px 0 0}

/* blog */
.blog{top:3411px;height:546px;background:linear-gradient(180deg,#dbe9f7 0%,#eef5fc 100%);border-radius:140px 0 140px 140px}
.blog .sec-title{position:absolute;top:72px;width:100%;text-transform:none;font-size:34px}
.posts{left:61px;top:160px;display:flex;gap:26px}
.post{width:250px}
.post-img{height:182px;border-radius:22px}
.post h4{font-size:14px;color:var(--ink);margin-top:22px}
.post p{font-size:11px;line-height:19px;margin-top:10px}
.post .more{display:block;margin-top:14px;font-size:13px;color:var(--blue);text-decoration:underline;font-family:"Raleway",sans-serif}

/* trusted */
.trusted{top:3957px;height:434px}
.trusted .sec-title{position:absolute;top:66px;width:100%}
.logos{left:215px;top:185px;display:grid;grid-template-columns:repeat(5,154px);grid-auto-rows:96px}
.logo{display:flex;align-items:center;justify-content:center;font-family:"Raleway",sans-serif;font-size:14px;font-weight:600;color:var(--ink);text-align:center;border-right:1px solid var(--line);padding:0 8px}
.logo:nth-child(5n){border-right:0}
.logo:nth-child(-n+5){border-bottom:1px solid var(--line)}
.logo i{width:12px;height:12px;border-radius:50%;background:var(--blue-mid);margin-right:7px;flex:none}

/* footer */
.footer{top:4391px;height:375px;background:var(--navy);color:#d5dded}
.fcol{top:54px;width:250px}
.fcol h4{font-size:17px;color:#fff;text-transform:uppercase;margin-bottom:16px}
.fcol ul{list-style:none;font-size:11px;line-height:21px}
.fcol li::before{content:"";display:inline-block;width:4px;height:4px;border-radius:50%;background:var(--sky);margin-right:10px;vertical-align:middle}
.contact-row{display:flex;align-items:center;gap:14px;font-size:12px;margin-bottom:12px}
.footer-rule{left:61px;right:61px;top:321px;height:1px;background:rgba(255,255,255,.15)}
.legal{left:61px;top:338px;font-size:10.5px}
.legal .accent{color:var(--sky)}
.legal-links{right:61px;top:338px;font-size:10.5px;display:flex;gap:12px}
</style>
</head>
<body>

<header class="section site-header">
  <div class="abs brand">RMV</div>
  <nav class="abs nav-top"><span>PARTNERS</span><span>BLOG</span><span>ABOUT US</span><span>CONTACT US</span></nav>
  <div class="abs nav-rule"></div>
  <nav class="abs nav-main"><span class="on">HOME</span><span>CLOUD</span><span>SERVICES</span><span>SOFTWARE</span></nav>
</header>

<section class="section hero">
  <div class="abs hero-art" role="img" aria-label="Glowing blue cloud with an up and down arrow over a city skyline"></div>
  <h1 class="abs">Operating<br>under a cloud ?</h1>
  <div class="abs hero-sub">THERE'S A SILVER LINING</div>
  <div class="abs tiles">
    <div class="tile">
      <svg width="50" height="44" viewBox="0 0 50 44" fill="none" stroke="#fff" stroke-width="1.6"><path d="M4 8 L18 22 L28 14 L44 30"/><path d="M38 30h6v-6"/><rect x="16" y="30" width="18" height="12"/><path d="M16 36h18"/></svg>
      REDUCING<br>COST
    </div>
    <div class="tile">
      <svg width="50" height="44" viewBox="0 0 50 44" fill="none" stroke="#fff" stroke-width="1.6"><rect x="6" y="24" width="16" height="16"/><rect x="28" y="24" width="16" height="16"/><path d="M14 24v-8h22v8"/><path d="M18 8a9 9 0 0 1 14 0"/><path d="M21 12a5 5 0 0 1 8 0"/></svg>
      MIGRATION
    </div>
    <div class="tile">
      <svg width="50" height="44" viewBox="0 0 50 44" fill="none" stroke="#fff" stroke-width="1.6"><path d="M3 18 L13 10 L22 14 L30 10 L47 18"/><path d="M13 22 L24 32 Q27 34 29 31 L37 24"/><path d="M20 14 L30 22"/></svg>
      WORK<br>WITH US
    </div>
  </div>
</section>

<section class="section promise">
  <h2 class="sec-title">Did the promise of cloud <span class="accent">computing<br>happen for you?</span></h2>
  <div class="abs promise-copy">
    <p>We didn't think so! You're not alone. There are may companies just like you who believed in the promise of cloud computing but are now shackled by it.</p>
    <p class="accent">But there is a silver lining, reduce costs and simplify their operationas a result.</p>
    <p class="lead">It can besummarised in threee promises RMV<br>makes to every client or Partner:</p>
    <ol>
      <li>You can <span class="accent">reduce cloud cost</span>. Without needing to move supplier</li>
      <li>You can <span class="accent">migrate</span> from one cloud to another more easily</li>
      <li>You can <span class="accent">simplify</span>, your cloud management and choose your favoured provider</li>
    </ol>
    <p class="call">If you already know or want to talk to just call</p>
  </div>
  <div class="abs promise-btns">
    <span class="btn btn-outline"><svg width="18" height="18" viewBox="0 0 24 24" fill="none" stroke="currentColor" stroke-width="2"><path d="M5 3h4l2 5-3 2a12 12 0 0 0 6 6l2-3 5 2v4a2 2 0 0 1-2 2A18 18 0 0 1 3 5a2 2 0 0 1 2-2z"/></svg>01632 960 418</span>
    <span class="btn btn-solid">SEND AN EMAIL</span>
  </div>
  <div class="abs device" role="img" aria-label="Laptop showing a cloud cost dashboard with a bar chart"></div>
  <div class="abs device-base"></div>
</section>

<section class="section tools">
  <div class="abs tools-art" role="img" aria-label="Network of service icons circling a central cloud"></div>
  <h2 class="abs">Your cloud, your tools</h2>
  <p class="abs">A Suite Of Software to Simplify Deployment</p>
  <span class="btn">CLOUD SOFTWARE</span>
</section>

<section class="section move">
  <h2 class="sec-title">How hard is it to move<br><span class="accent">your cloud?</span></h2>
  <svg class="abs arrow" style="left:126px" width="16" height="30" viewBox="0 0 16 30" fill="none" stroke="#222" stroke-width="1.8"><path d="M14 2 L2 15 L14 28"/></svg>
  <svg class="abs arrow" style="left:1058px" width="16" height="30" viewBox="0 0 16 30" fill="none" stroke="#222" stroke-width="1.8"><path d="M2 2 L14 15 L2 28"/></svg>
  <div class="abs cards">
    <div class="card"><div class="name">Nimbra</div><p>Lorem Ipsum has been the industry's standard dummy text ever since the, when an unknown printer</p><span class="btn btn-solid">LEARN MORE</span></div>
    <div class="card"><div class="name">Cirrova</div><p>Lorem Ipsum has been the industry's standard dummy text ever since the, when an unknown printer</p><span class="btn btn-solid">LEARN MORE</span></div>
    <div class="card"><div class="name">Altoscale</div><p>Lorem Ipsum has been the industry's standard dummy text ever since the, when an unknown printer</p><span class="btn btn-solid">LEARN MORE</span></div>
  </div>
</section>

<section class="section advice">
  <h2 class="sec-title">Knowledgeable independent<br><span class="accent">advice matters</span></h2>
  <div class="abs advice-copy">
    <p>Traditionally, the balance of power lies with your host, who has no interest in you moving to another platform. It may also be that your cloud supplier is a linked to your IT firm, Developer or even staff preferences - and in some cases they will specialise in only one of these suppliers.</p>
    <p>It's time to break free. RMV equips companies, resellers and consultants with the power to choose, to negotiate, to move. We can do this for you.</p>
  </div>
</section>

<section class="section costs">
  <h2 class="sec-title">Make your cloud costs<br><span class="accent">evaporate</span></h2>
  <svg class="abs ring" width="186" height="186" viewBox="0 0 186 186">
    <circle cx="93" cy="93" r="84" fill="none" stroke="#ffffff" stroke-width="6"/>
    <path d="M93 9 A84 84 0 1 0 177 93" fill="none" stroke="#1673cc" stroke-width="6"/>
    <text x="93" y="90" text-anchor="middle" font-family="Raleway" font-size="32" font-weight="500" fill="#fff">20%</text>
    <text x="93" y="120" text-anchor="middle" font-family="Raleway" font-size="20" fill="#1673cc">CHEAPER</text>
  </svg>
  <div class="abs cost-copy">
    <p>As cloud costs continue to escalate, and as you suddenly hit new tiers of spend, you may feel helpless in the face of rising costs.</p>
    <p>However, even taking the cost of moving into account, RMV has estimated the average client will save 20% of spend on their cloud by using us to find the best solution and help you to move there.</p>
  </div>
  <span class="btn">SEE CASE STUDIES</span>
</section>

<section class="section start">
  <h2 class="abs">Let's get <span class="accent">started</span></h2>
  <p class="abs">If You would like to speak to a friendly and helpful member of our team, ask question, discuss option or to help with anything on your mind, please get in touch.</p>
  <div class="abs start-btns">
    <span class="btn btn-outline"><svg width="18" height="18" viewBox="0 0 24 24" fill="none" stroke="currentColor" stroke-width="2"><path d="M5 3h4l2 5-3 2a12 12 0 0 0 6 6l2-3 5 2v4a2 2 0 0 1-2 2A18 18 0 0 1 3 5a2 2 0 0 1 2-2z"/></svg>01632 960 418</span>
    <span class="btn btn-solid">SEND AN EMAIL</span>
  </div>
  <div class="abs person" role="img" aria-label="Businessman in a suit using a tablet"></div>
</section>

<section class="section blog">
  <h2 class="sec-title">RMV <span class="accent">Blog</span></h2>
  <div class="abs posts">
    <article class="post"><div class="post-img" role="img" aria-label="Hands holding a tablet showing a cloud icon" style="background:linear-gradient(135deg,#1d2a36,#5a7a8e)"></div><h4>Lorem Ipsum has been the Text !</h4><p>Lorem Ipsum has been the indus standard dummy text ever since the, when an this unknown printer took a galley.</p><a class="more">Read More ▸</a></article>
    <article class="post"><div class="post-img" role="img" aria-label="Two colleagues working at a monitor" style="background:linear-gradient(135deg,#0e2a52,#6b8fb8)"></div><h4>Lorem Ipsum has been the Text !</h4><p>Lorem Ipsum has been the indus standard dummy text ever since the, when an this unknown printer took a galley.</p><a class="more">Read More ▸</a></article>
    <article class="post"><div class="post-img" role="img" aria-label="Hand holding a phone under a digital cloud" style="background:linear-gradient(135deg,#2a6fb8,#a9d1f0)"></div><h4>Lorem Ipsum has been the Text !</h4><p>Lorem Ipsum has been the indus standard dummy text ever since the, when an this unknown printer took a galley.</p><a class="more">Read More ▸</a></article>
    <article class="post"><div class="post-img" role="img" aria-label="Cable plugged into a white cloud against blue sky" style="background:linear-gradient(135deg,#1c4f96,#dfe9f3)"></div><h4>Lorem Ipsum has been the Text !</h4><p>Lorem Ipsum has been the indus standard dummy text ever since the, when an this unknown printer took a galley.</p><a class="more">Read More ▸</a></article>
  </div>
</section>

<section class="section trusted">
  <h2 class="sec-title">Trusted <span class="accent">by</span></h2>
  <div class="abs logos">
    <div class="logo"><i></i>Harrowby</div>
    <div class="logo">Civic Works Office</div>
    <div class="logo"><i></i>Opticon Trust</div>
    <div class="logo">Roadline Agency</div>
    <div class="logo">Kaitora</div>
    <div class="logo"><i></i>Clearsight</div>
    <div class="logo">Marlow Studio</div>
    <div class="logo">Aster Youth Foundation</div>
    <div class="logo"><i></i>Parcelpoint</div>
    <div class="logo">Spokely</div>
  </div>
</section>

<footer class="section footer">
  <div class="abs fcol" style="left:61px"><h4>Cloud Services</h4><ul><li>Nimbra</li><li>Cirrova</li><li>Altoscale</li><li>Ferrocore</li><li>Quillon</li><li>Bluereef Compute</li><li>Others</li><li>Private Cloud</li></ul></div>
  <div class="abs fcol" style="left:337px"><h4>Services</h4><ul><li>Cloud Cost Review</li><li>Migration Planning</li><li>Migration Execution</li><li>Security &amp; Compliance</li></ul>
    <h4 style="margin-top:32px">Software</h4><ul><li>Skyhatch</li><li>ShiftArc</li></ul></div>
  <div class="abs fcol" style="left:614px"><h4>About RMV</h4><ul><li>Blog</li><li>Partners</li><li>About Us</li><li>Contact Us</li></ul></div>
  <div class="abs fcol" style="left:889px"><h4>Connect</h4>
    <div class="contact-row"><svg width="18" height="18" viewBox="0 0 24 24" fill="none" stroke="#2f9be0" stroke-width="2"><path d="M5 3h4l2 5-3 2a12 12 0 0 0 6 6l2-3 5 2v4a2 2 0 0 1-2 2A18 18 0 0 1 3 5a2 2 0 0 1 2-2z"/></svg><span style="font-size:14px">01632 960 418</span></div>
    <div class="contact-row"><svg width="18" height="14" viewBox="0 0 18 14" fill="none" stroke="#2f9be0" stroke-width="1.6"><rect x="1" y="1" width="16" height="12"/><path d="M1 1 L9 8 L17 1"/></svg><span>Email Us</span></div>
    <div class="contact-row"><span style="width:16px;height:16px;background:#2f9be0;display:inline-block"></span><span>Network Profile</span></div>
    <ul style="margin-top:18px"><li>Alder House</li><li>Mill Road</li><li>Eastbrook</li><li>EB4 2QX England</li></ul>
  </div>
  <div class="abs footer-rule"></div>
  <div class="abs legal">©<span class="accent">RMV Group Limited</span>. All rights reserved.</div>
  <div class="abs legal-links"><span>Sitemap</span><span>|</span><span>Terms of Use</span><span>|</span><span>Privacy Policy</span><span>|</span><span>Contact Us</span></div>
</footer>

</body>
</html>
```